Box Designs for a Christian project

Am looking for innovative creative designs for my box project. The boxes comprise of one big box and 6 small boxes. The size of the big box is L160*W113*D95 mm and the size of small boxes are L150*W89*D16 m. Am looking for something colorful and bright that integrates christian themes and things like beautiful landscapes, resting animals etc and uses colors like electric blue, sky-blue, green yellow, electric purple and orange/yellow. The big box should have the text "Merrow Glade" and for the small boxes use titles "pony", "horse" "dog" "cat" " parrot" "sparrow". I will obviously change the name when I select the final design.

Font styles to use
Script

Colors
6b449b
ec1f27
00a990
fbed22
f78f20
0393ce

Requirements
Must have
• Bright innovative colors

```html
<!DOCTYPE html>
<html lang="en">
<head>
<meta charset="utf-8">
<title>Merrow Glade – Box Set Artwork</title>
<link href="https://fonts.googleapis.com/css2?family=Sacramento&display=swap" rel="stylesheet">
<style>
  :root {
    --backdrop: #d9dadc;
    --paper: #ffffff;
    --rule: #c9c9cc;
    --script-purple: #5e2f91;
    --sky-top: #2fb7d6;
    --sky-glow: #eef7a8;
    --hill-light: #9fd83a;
    --hill-deep: #2f8a1e;
  }
  * { margin: 0; padding: 0; box-sizing: border-box; }
  html, body {
    width: 1200px;
    height: 1200px;
    overflow: hidden;
    background: var(--backdrop);
  }
  .artboard {
    position: relative;
    width: 1200px;
    height: 1200px;
  }
  .spine-labels {
    position: absolute;
    left: 14px;
    top: 334px;
    width: 609px;
    height: 390px;
    background: var(--paper);
    border: 1px solid var(--rule);
    display: flex;
    flex-direction: column;
  }
  .spine-label {
    flex: 1;
    display: flex;
    align-items: center;
    justify-content: center;
    overflow: hidden;
    border-bottom: 1px solid var(--rule);
    font-family: "Sacramento", cursive;
    font-size: 44px;
    font-weight: 400;
    line-height: 1;
    color: var(--script-purple);
  }
  .spine-label:last-child { border-bottom: none; }
  .lid-panel {
    position: absolute;
    left: 646px;
    top: 332px;
    width: 549px;
    height: 388px;
    background: var(--paper);
  }
  .lid-artwork {
    position: absolute;
    left: 32px;
    top: 33px;
    width: 484px;
    height: 322px;
    border-radius: 10px;
    background:
      radial-gradient(ellipse 40% 35% at 48% 38%, rgba(255,255,240,0.95), rgba(255,255,240,0) 70%),
      linear-gradient(180deg, var(--sky-top) 0%, #8fd6c8 30%, var(--sky-glow) 52%, var(--hill-light) 66%, var(--hill-deep) 100%);
  }
  .name-panel {
    position: absolute;
    left: 650px;
    top: 738px;
    width: 544px;
    height: 146px;
    background: var(--paper);
    display: flex;
    align-items: center;
    justify-content: center;
    overflow: hidden;
  }
  .brand-name {
    font-family: "Sacramento", cursive;
    font-size: 72px;
    font-weight: 400;
    line-height: 1;
    color: var(--script-purple);
    white-space: nowrap;
  }
</style>
</head>
<body>
  <main class="artboard">
    <section class="spine-labels" aria-label="Small box spine labels">
      <div class="spine-label">Pony</div>
      <div class="spine-label">Horse</div>
      <div class="spine-label">Dog</div>
      <div class="spine-label">Cat</div>
      <div class="spine-label">Parrot</div>
      <div class="spine-label">Sparrow</div>
    </section>

    <section class="lid-panel">
      <div class="lid-artwork" role="img" aria-label="Illustration of a cross draped in purple cloth on a green hill, with sunburst, bokeh lights and rolling meadows under a bright blue sky"></div>
    </section>

    <section class="name-panel">
      <h1 class="brand-name">Merrow Glade</h1>
    </section>
  </main>
</body>
</html>
```